Plakat-Design für Vereinsfest
Zielgruppe
Unser Verein veranstaltet jedes Jahr im August das Vereinsfest 'Sonnwendtag', das in einem kleinen Wäldchen innerhalb des Heimatortes stattfindet. Am Samstag und Sonntag sorgen verschiedene Musikgruppen für Unterhaltung. Es soll ein Veranstaltungsplakat gestaltet werden, dass sich an die Vorgaben (siehe unten) hält und die Veranstaltung bewirbt.
Zielgruppe sind Bürger des Heimatortes.
Aufgabenstellung
Das Vereinslogo ist beigefügt und sollte prominent auf dem Plakat vertreten sein, Logo und Schriftzug können auch getrennt oder anders angeordnet werden. Der Veranstaltungstitel lautet "Sonnwendtag", es findet am 20. und 21. August "Am Hirtenstein" (Veranstaltungsort) statt.
Programmpunkte: Samstag: Musikalische Unterhaltung mit den Bachpfeifern; Sonntag: Musikalische Unterhaltung mit den Moorbachrabauken
Uhrzeiten sollten enthalten sein:
Beginn Samstag: ab 15 Uhr
Beginn Sonntag: ab 10 Uhr
Das Plakat soll gut leserlich auch aus der Entfernung sein, da es an Straßen plakatiert wird.
Das Plakat soll für spätere Jahre editierbar sein.
Schriftart im Logo: Californian FB Bold (muss aber nicht auf andere Textelemente angewendet werden). Das Plakat soll in DIN A2 gedruckt werden. Die Webadresse sollte auf dem Plakat stehen.

```html
<!DOCTYPE html>
<html lang="de">
<head>
<meta charset="utf-8">
<title>Sonnwendtag – Plakat</title>
<link rel="stylesheet" href="https://fonts.googleapis.com/css2?family=Abril+Fatface&family=Libre+Caslon+Text:wght@400;700&display=swap">
<style>
  :root {
    --page-bg: #e6e5e2;
    --paper: #f2f1ee;
    --blue: #1a6396;
    --blue-dark: #124e7a;
    --navy: #1f2a6b;
    --grey-dark: #4a4a4a;
    --grey-text: #3d3d3d;
    --white: #ffffff;
  }
  * { box-sizing: border-box; margin: 0; padding: 0; }
  html, body { width: 1200px; height: 1194px; overflow: hidden; }
  body {
    background: var(--page-bg);
    font-family: "Libre Caslon Text", Georgia, serif;
    position: relative;
  }
  .poster {
    position: absolute;
    left: 180px; top: 22px;
    width: 840px; height: 1150px;
    background: var(--paper);
    box-shadow: 0 2px 10px rgba(0,0,0,.12);
  }
  .frame-outer, .frame-inner {
    position: absolute;
    border: 3px solid var(--blue);
  }
  .frame-outer { inset: 14px; }
  .frame-inner { inset: 22px; border-width: 1.5px; }
  .ornament {
    position: absolute;
    width: 110px; height: 110px;
    background: radial-gradient(circle at center, rgba(26,99,150,.22), rgba(26,99,150,0) 70%);
  }
  .ornament.tl { left: 30px; top: 30px; }
  .ornament.tr { right: 30px; top: 30px; }
  .ornament.bl { left: 30px; bottom: 30px; }
  .ornament.br { right: 30px; bottom: 30px; }

  .club {
    position: absolute;
    top: 80px; left: 0; right: 0;
    display: flex; justify-content: center; align-items: center; gap: 22px;
  }
  .club-mark {
    width: 118px; height: 118px; border-radius: 50%;
    background: var(--navy);
    opacity: .85;
  }
  .club-name {
    color: var(--navy);
    font-weight: 400;
    font-size: 30px;
    line-height: 1.05;
  }
  .club-name span { display: block; }
  .club-name .small { font-size: 15px; }

  .title {
    position: absolute;
    top: 262px; left: 0; right: 0;
    text-align: center;
    font-family: "Abril Fatface", "Bodoni Moda", serif;
    font-size: 104px;
    color: var(--blue);
    letter-spacing: -2px;
    line-height: 1;
  }

  .date-band {
    position: absolute;
    top: 446px; left: 58px; right: 58px; height: 112px;
    background: var(--blue);
    color: var(--white);
    text-align: center;
    padding-top: 10px;
  }
  .date-band .date { font-weight: 700; font-size: 48px; line-height: 1.1; }
  .date-band .place { font-size: 32px; line-height: 1.25; }

  .programme {
    position: absolute;
    top: 588px; left: 70px; right: 70px;
    display: flex; justify-content: space-between;
    text-align: center;
  }
  .day { width: 340px; }
  .day h2 {
    font-size: 30px; font-weight: 700; color: var(--grey-text);
    line-height: 1.15;
  }
  .day p {
    font-size: 24px; font-weight: 700; color: var(--blue);
    line-height: 1.4;
  }

  .times {
    position: absolute;
    top: 810px; left: 50%; transform: translateX(-50%);
    width: 340px; height: 80px;
    background: var(--grey-dark);
    color: var(--white);
    font-size: 22px;
    text-align: center;
    line-height: 1.3;
    padding-top: 10px;
    border: 1px solid #2e2e2e;
  }

  .band-illustration {
    position: absolute;
    top: 900px; left: 150px; right: 150px; height: 180px;
    background: linear-gradient(180deg, rgba(26,99,150,.1), rgba(18,78,122,.55));
    border-radius: 4px;
  }

  .web {
    position: absolute;
    bottom: 30px; left: 0; right: 0;
    text-align: center;
    font-size: 24px; font-weight: 700;
    color: var(--grey-text);
  }
</style>
</head>
<body>
  <main class="poster">
    <div class="frame-outer"></div>
    <div class="frame-inner"></div>
    <div class="ornament tl" role="img" aria-label="Verschnörkeltes Eckornament"></div>
    <div class="ornament tr" role="img" aria-label="Verschnörkeltes Eckornament"></div>
    <div class="ornament bl" role="img" aria-label="Verschnörkeltes Eckornament"></div>
    <div class="ornament br" role="img" aria-label="Verschnörkeltes Eckornament"></div>

    <header class="club">
      <div class="club-mark"></div>
      <div class="club-name">
        <span class="small">Historische</span>
        <span>Stadtwache <span class="small" style="display:inline">und</span></span>
        <span>Trachtengruppe</span>
        <span>Lindenau <span class="small" style="display:inline">e.V.</span></span>
      </div>
    </header>

    <h1 class="title">SONNWENDTAG</h1>

    <section class="date-band">
      <div class="date">20 - 21 August</div>
      <div class="place">“Am Hirtenstein”</div>
    </section>

    <section class="programme">
      <div class="day">
        <h2>SAMSTAG:</h2>
        <p>Musikalische<br>Unterhaltung mit den<br>Bachpfeifern</p>
      </div>
      <div class="day">
        <h2>SONNTAG:</h2>
        <p>Musikalische<br>Unterhaltung mit den<br>Moorbachrabauken</p>
      </div>
    </section>

    <div class="times">
      Beginn Samstag: ab 15 Uhr<br>
      Beginn Sonntag: ab 10 Uhr
    </div>

    <div class="band-illustration" role="img" aria-label="Silhouetten einer Blaskapelle mit Notenlinien"></div>

    <footer class="web">www.stadtwache-lindenau.de</footer>
  </main>
</body>
</html>
```